Tembra waste and recycling needs a thank you for business card

We need to design a thank you card for our customers who purchase with us. I like black gloss front and back with thankyou on the front. Or white gloss front back.
The inside should be white and maybe our logo on the bottom right hand side (as you open it up). Maybe put some more pictures on it.

On the inside of the card write -
Congratulations on your recent purchase.
Customers like YOU are the foundation of our business.
We appreciate having YOU as a customer and we look forward to providing you with the best possible service into the future.

PS as an added value if you refer any purchasing clients to Tembra YOU will receive one years free document destruction to the value of $204 or $164 towards a waste and recycling credit. Prices include GST.

Warm Regards,

Dorian Quellsby, Business Owner.

Target Market(s)

Business customers within Australia

Industry/Entity Type

Recycling

Colors

Designer to choose colors to be used in the design.

Requirements
Must have
• 'thank you' on the front

'Congratulations on your recent purchase..........' exact text as in project overview. This is to appear on the inside page.

Our logo to be small on the bottom of the inside somewhere
Nice to have
• some more of our pictures

```html
<!DOCTYPE html>
<html lang="en">
<head>
<meta charset="utf-8">
<title>Tembra Waste &amp; Recycling – Thank You Card</title>
<link href="https://fonts.googleapis.com/css2?family=Mali:ital,wght@1,400;1,500&family=Saira+Stencil+One&family=Arimo:wght@400;700&display=swap" rel="stylesheet">
<style>
  :root {
    --teal: #0f747b;
    --teal-soft: rgba(255,255,255,0.18);
    --ink: #333333;
    --paper: #ffffff;
    --frame: #8a8a8a;
    --brand-dark: #1a1a1a;
  }
  * { margin: 0; padding: 0; box-sizing: border-box; }
  html, body { width: 1200px; height: 526px; overflow: hidden; background: var(--paper); }
  .canvas { position: relative; width: 1200px; height: 526px; }

  .card-front {
    position: absolute; left: 60px; top: 81px; width: 506px; height: 337px;
    background: var(--teal); overflow: hidden;
  }
  .front-emblem {
    position: absolute; left: 173px; top: 30px; width: 240px; height: 270px;
  }
  .front-title {
    position: absolute; left: 0; right: 0; top: 132px; text-align: center;
    font-family: "Saira Stencil One", sans-serif; font-size: 52px; letter-spacing: 1px;
    color: var(--paper); line-height: 1;
  }

  .card-inside {
    position: absolute; left: 633px; top: 85px; width: 507px; height: 337px;
    background: var(--paper); border: 1px solid var(--frame);
  }
  .message {
    position: absolute; left: 0; right: 0; top: 55px; text-align: center;
    font-family: "Mali", cursive; font-style: italic; color: var(--teal);
    font-size: 13.5px; line-height: 1.25;
  }
  .message p { margin-bottom: 11px; }
  .message p.lead-wide { margin-bottom: 0; }
  .postscript {
    position: absolute; left: 64px; width: 400px; top: 165px;
    font-family: "Mali", cursive; font-style: italic; color: var(--ink);
    font-size: 9.6px; line-height: 1.22;
  }
  .postscript .ps-mark { font-size: 13px; }
  .sign-off, .signatory {
    position: absolute; left: 64px;
    font-family: "Mali", cursive; font-style: italic; color: var(--ink); font-size: 10.5px;
  }
  .sign-off { top: 223px; }
  .signatory { top: 268px; line-height: 1.45; }

  .brand {
    position: absolute; left: 262px; top: 215px; display: flex; align-items: center; gap: 10px;
  }
  .brand-name {
    font-family: "Arimo", sans-serif; font-weight: 700; font-size: 27px;
    color: var(--brand-dark); letter-spacing: 0.5px;
  }
  .brand-mark { width: 52px; height: 52px; border-radius: 50%; background: var(--teal); }

  .contact {
    position: absolute; top: 289px; left: 252px;
    font-family: "Arimo", sans-serif; font-size: 10.5px; color: var(--brand-dark);
    display: flex; gap: 20px;
  }
</style>
</head>
<body>
<div class="canvas">
  <section class="card-front">
    <svg class="front-emblem" viewBox="0 0 240 270" role="img" aria-label="Faint recycling arrows symbol behind the title">
      <circle cx="120" cy="140" r="118" fill="var(--teal-soft)"/>
    </svg>
    <h1 class="front-title">THANK YOU</h1>
  </section>

  <section class="card-inside">
    <div class="message">
      <p>Congratulations on your recent purchase.</p>
      <p>Customers like YOU are the foundation of our business.</p>
      <p class="lead-wide">We appreciate having YOU as a customer and we look forward<br>to providing you with the best possible service into the future.</p>
    </div>

    <p class="postscript"><span class="ps-mark">PS</span> as an added value if you refer any purchasing clients to Tembra YOU will receive one years free document destruction to the value of $204 or $164 towards a waste and recycling credit.<br>Prices include GST.</p>

    <p class="sign-off">Warm regards,</p>
    <p class="signatory">Dorian Quellsby,<br>Business Owner</p>

    <div class="brand">
      <span class="brand-name">TEMBRA</span>
      <span class="brand-mark"></span>
    </div>

    <div class="contact">
      <span class="contact-email">sales@tembrawaste.com.au</span>
      <span class="contact-phone">08 7031 4290</span>
    </div>
  </section>
</div>
</body>
</html>
```